Graphics for New Online Software

Looking at a designer to design a UI/UX Interface for an Online Events Platform (just JPEG) and some corresponding images for a website content (i.e. features etc)

Deliverables:
1x User Interface Design for the Platform (refer to attachment)
5-6x Feature Listing Images (refer to attachment)

Target Market(s)

Technology, Online Users Etc

Industry/Entity Type

Software Developer

Number of Pages Required

1 page

Font styles to use
Sans Serif

Colors
34a7d8
0493ce
3176b5
85acd3

Requirements
Must have
• Looks like a well built software - examples:
https://velmora.io/
https://quillard.com/

All the images should look very professional, as though you are using it on the online platform itself.
Nice to have
• Refer to attached "Feature Listing" and Logo

```html
<!DOCTYPE html>
<html lang="en">
<head>
<meta charset="utf-8">
<title>Stagewell – Platform Screens</title>
<link href="https://fonts.googleapis.com/css2?family=Lato:wght@400;700;900&display=swap" rel="stylesheet">
<style>
:root{
  --stage-bg:#1e1e1e;
  --side-top:#2a5fab;
  --side-bottom:#1584cb;
  --side-active:#3f88cf;
  --main-bg:#f1f1f1;
  --card:#ffffff;
  --tile:#f0f0f1;
  --ink:#1c1c1c;
  --body:#3a3a3a;
  --brand:#2f6fb6;
  --brand-bright:#3176b5;
  --line:#d6d6d6;
  --soft:#85acd3;
}
*{box-sizing:border-box;margin:0;padding:0}
html,body{width:1200px;height:754px;overflow:hidden}
body{background:var(--stage-bg);font-family:'Lato',sans-serif;position:relative;color:var(--ink)}

.screen{position:absolute;width:548px;height:337px;background:var(--main-bg);overflow:hidden}
.screen--info{left:40px;top:28px}
.screen--expo{left:620px;top:28px}
.screen--rewards{left:330px;top:389px}

.sidebar{position:absolute;left:0;top:0;width:128px;height:100%;background:linear-gradient(180deg,var(--side-top),var(--side-bottom))}
.brand{position:absolute;left:27px;top:38px;display:flex;align-items:center;gap:5px;color:#fff;font-weight:900;font-size:15px;letter-spacing:-.2px}
.brand__dot{width:9px;height:9px;border-radius:50%;background:#fff}
.nav{position:absolute;left:0;top:75px;width:128px;list-style:none}
.nav__item{position:relative;height:27px;display:flex;align-items:center;padding-left:27px;color:#fff;font-size:5.6px;font-weight:700;letter-spacing:.2px}
.nav__item::before{content:"»";width:15px;font-size:6px;opacity:.9}
.nav__item--active{background:var(--side-active);height:23px;margin:2px 0}
.nav__item--active::after{content:"";position:absolute;right:0;top:5px;border:6px solid transparent;border-right:6px solid var(--side-bottom);border-left:0;opacity:.55}
.copyright{position:absolute;left:27px;top:304px;color:#e6f0fa;font-size:5.3px;line-height:9.5px}

.duration{position:absolute;right:33px;top:39px;font-size:7.4px;font-weight:700;color:var(--ink)}
.duration span{color:var(--brand-bright);margin-left:2px}
.page-no{position:absolute;right:8px;top:323px;font-size:5.4px;color:#333}

.card{position:absolute;left:145px;top:36px;width:370px;height:264px;background:var(--card);border-radius:6px;box-shadow:0 1px 5px rgba(0,0,0,.12)}
.card__title{position:absolute;left:11px;top:12px;font-size:11.5px;font-weight:900;letter-spacing:.2px}
.card__rule{position:absolute;left:11px;right:11px;top:34px;height:1px;background:var(--line)}

.section-title{position:absolute;left:0;right:0;top:45px;text-align:center;color:var(--brand);font-size:11px;font-weight:900;letter-spacing:.3px}
.speaker{position:absolute;width:170px;height:85px;background:var(--tile);border-radius:6px}
.speaker__photo{position:absolute;left:9px;top:13px;width:59px;height:59px;border-radius:5px}
.speaker__name{position:absolute;left:77px;top:11px;color:var(--brand);font-size:9.6px;font-weight:700}
.speaker__bio{position:absolute;left:77px;top:27px;color:var(--body);font-size:6.5px;line-height:10.5px}
.speaker__social{position:absolute;left:77px;top:64px;display:flex;gap:7px}
.speaker__social i{width:6px;height:6px;border-radius:50%;background:#1c1c1c;display:block}

.note{position:absolute;top:46px;width:142px;height:42px;background:var(--tile);border-radius:5px;box-shadow:0 1px 3px rgba(0,0,0,.12);text-align:center;font-size:7.4px;font-weight:700;line-height:13px;padding-top:8px}
.note a{color:var(--brand);text-decoration:underline}
.flow-arrow{position:absolute;left:258px;top:60px}
.expo-art{position:absolute;left:58px;top:100px;width:258px;height:154px;border-radius:6px;background:radial-gradient(ellipse at 50% 55%,#f3dcc0 0%,#e9eef6 55%,#ffffff 100%)}

.task{position:absolute;left:11px;width:142px;height:25px;display:flex;align-items:center;border-bottom:1px solid var(--line)}
.task:last-of-type{border-bottom:0}
.task__check{width:17px;height:17px;border:1px solid var(--brand);border-radius:50%;display:flex;align-items:center;justify-content:center;margin-right:8px}
.task__label{color:var(--brand);font-size:8px;font-weight:700}
.points{position:absolute;left:11px;top:142px;font-size:13px;font-weight:700;color:#333}
.points b{color:var(--brand);font-weight:900}
.collect{position:absolute;left:11px;top:173px;font-size:8.4px;font-weight:700}
.claim{position:absolute;left:11px;top:197px;font-size:6.5px;line-height:12.5px;color:var(--body)}
.claim b{color:var(--brand);font-weight:700}
.gift-art{position:absolute;left:248px;top:50px;width:96px;height:146px;border-radius:6px;background:radial-gradient(circle at 50% 62%,#f3a52f 0%,#e54b3a 30%,#e9eef6 62%,#ffffff 100%)}
</style>
</head>
<body>

<!-- Event info screen -->
<section class="screen screen--info">
  <aside class="sidebar">
    <div class="brand"><span class="brand__dot"></span>STAGEWELL</div>
    <ul class="nav">
      <li class="nav__item nav__item--active">EVENT INFO</li>
      <li class="nav__item">STAGE</li>
      <li class="nav__item">BREAKOUTS</li>
      <li class="nav__item">BOOTHS</li>
      <li class="nav__item">VIRTUAL EXHIBITION</li>
      <li class="nav__item">REWARDS</li>
    </ul>
    <p class="copyright">Copyright © 2020 Company Name.<br>All Right Reserved</p>
  </aside>
  <p class="duration">Event Duration: <span>(Remaining 12:35)</span></p>
  <div class="card">
    <h2 class="card__title">EVENT INFO</h2>
    <div class="card__rule"></div>
    <h3 class="section-title">SPEAKERS</h3>
    <article class="speaker" style="left:11px;top:68px">
      <div class="speaker__photo" role="img" aria-label="Speaker portrait photo" style="background:linear-gradient(160deg,#dfe3e8,#3b4a63)"></div>
      <h4 class="speaker__name">Name Heading</h4>
      <p class="speaker__bio">Neque porro quisquam<br>est qui dolorem ipsum<br>quia dolor sit amet</p>
      <div class="speaker__social"><i></i><i></i><i></i></div>
    </article>
    <article class="speaker" style="left:189px;top:68px">
      <div class="speaker__photo" role="img" aria-label="Speaker portrait photo" style="background:linear-gradient(160deg,#e9e6e2,#b98a62)"></div>
      <h4 class="speaker__name">Name Heading</h4>
      <p class="speaker__bio">Neque porro quisquam<br>est qui dolorem ipsum<br>quia dolor sit amet</p>
      <div class="speaker__social"><i></i><i></i><i></i></div>
    </article>
    <article class="speaker" style="left:11px;top:165px">
      <div class="speaker__photo" role="img" aria-label="Speaker portrait photo" style="background:linear-gradient(160deg,#e4e4e4,#2e3440)"></div>
      <h4 class="speaker__name">Name Heading</h4>
      <p class="speaker__bio">Neque porro quisquam<br>est qui dolorem ipsum<br>quia dolor sit amet</p>
      <div class="speaker__social"><i></i><i></i><i></i></div>
    </article>
    <article class="speaker" style="left:189px;top:165px">
      <div class="speaker__photo" role="img" aria-label="Speaker portrait photo" style="background:linear-gradient(160deg,#d8d8d8,#1f2733)"></div>
      <h4 class="speaker__name">Name Heading</h4>
      <p class="speaker__bio">Neque porro quisquam<br>est qui dolorem ipsum<br>quia dolor sit amet</p>
      <div class="speaker__social"><i></i><i></i><i></i></div>
    </article>
  </div>
  <p class="page-no">X10</p>
</section>

<!-- Virtual exhibition screen -->
<section class="screen screen--expo">
  <aside class="sidebar">
    <div class="brand"><span class="brand__dot"></span>STAGEWELL</div>
    <ul class="nav">
      <li class="nav__item">EVENT INFO</li>
      <li class="nav__item">STAGE</li>
      <li class="nav__item">BREAKOUTS</li>
      <li class="nav__item">BOOTHS</li>
      <li class="nav__item nav__item--active">VIRTUAL EXHIBITION</li>
      <li class="nav__item">REWARDS</li>
    </ul>
    <p class="copyright">Copyright © 2020 Company Name.<br>All Right Reserved</p>
  </aside>
  <p class="duration">Event Duration: <span>(Remaining 12:35)</span></p>
  <div class="card">
    <h2 class="card__title">VIRTUAL EXHIBITION</h2>
    <div class="card__rule"></div>
    <div class="note" style="left:27px">This is a nice image by Rhea.<br><a>Click Here</a> - website</div>
    <svg class="flow-arrow" width="12" height="12" viewBox="0 0 12 12" aria-hidden="true">
      <path d="M1 6h8M5.5 2L9.5 6 5.5 10" fill="none" stroke="#2f6fb6" stroke-width="2.2" stroke-linecap="round" stroke-linejoin="round"/>
    </svg>
    <div class="note" style="left:201px">More About this Picture &amp; Video<br><a>Find Out More</a></div>
    <div class="expo-art" role="img" aria-label="Isometric illustration of an exhibition hall with booths and visitors"></div>
  </div>
  <p class="page-no">X10</p>
</section>

<!-- Rewards screen -->
<section class="screen screen--rewards">
  <aside class="sidebar">
    <div class="brand"><span class="brand__dot"></span>STAGEWELL</div>
    <ul class="nav">
      <li class="nav__item">EVENT INFO</li>
      <li class="nav__item">STAGE</li>
      <li class="nav__item">BREAKOUTS</li>
      <li class="nav__item">BOOTHS</li>
      <li class="nav__item">VIRTUAL EXHIBITION</li>
      <li class="nav__item nav__item--active">REWARDS</li>
    </ul>
    <p class="copyright">Copyright © 2020 Company Name.<br>All Right Reserved</p>
  </aside>
  <p class="duration">Event Duration: <span>(Remaining 12:35)</span></p>
  <div class="card">
    <h2 class="card__title">REWARDS</h2>
    <div class="card__rule"></div>
    <div class="task" style="top:47px"><span class="task__check"><svg width="8" height="8" viewBox="0 0 8 8"><path d="M1.2 4.2l1.8 1.8 3.8-4" fill="none" stroke="#2f6fb6" stroke-width="1.4" stroke-linecap="round" stroke-linejoin="round"/></svg></span><span class="task__label">Visited Virtual Exhibition</span></div>
    <div class="task" style="top:72px"><span class="task__check"><svg width="8" height="8" viewBox="0 0 8 8"><path d="M1.2 4.2l1.8 1.8 3.8-4" fill="none" stroke="#2f6fb6" stroke-width="1.4" stroke-linecap="round" stroke-linejoin="round"/></svg></span><span class="task__label">Joined Breakout Room</span></div>
    <div class="task" style="top:97px;border-bottom:0"><span class="task__check"><svg width="8" height="8" viewBox="0 0 8 8"><path d="M1.2 4.2l1.8 1.8 3.8-4" fill="none" stroke="#2f6fb6" stroke-width="1.4" stroke-linecap="round" stroke-linejoin="round"/></svg></span><span class="task__label">Checked out Booths</span></div>
    <p class="points">Total Points: <b>40</b></p>
    <p class="collect">Collect Reward - Trigger Email/Link to 3rd Party App</p>
    <p class="claim">(Flash them a <b>PROMO CODE</b>/"Email will be given to you on how you can claim your prize)<br>They can go to www.prizelane.com to claim</p>
    <div class="gift-art" role="img" aria-label="Illustration of an opening gift box with confetti"></div>
  </div>
  <p class="page-no">X10</p>
</section>

</body>
</html>
```